exquisite label design for foam cleanser

Kindly invite you to design bottle label (102 mm*64 mm) for our product, a kind of foam cleanser for wearable aligners. The color of bottle and liquid inside are both clear, but the foam pump is white. You could download the pic of bottle among the uploaded files. I have no KV of our website or posters to supply you, except the logo file attached. Content on the label is attached too. Please check it. I wish the label would make our product look high-end and reliable. And it would be better if you could give some advice on paper material and special requirements for printing, related to your design. I value the texture of label too, because I think that stands for the quality of products. No color limitation for the use of our logo, and please ignore the Chinese characters in our logo, they are not in our plan.
Target Market(s)
16-35 female, orthodontic patients.
Colors
Designer to choose colors to be used in the design.
Look and feel
Each slider illustrates characteristics of the customer's brand and the style your logo design should communicate.

```html
<!DOCTYPE html>
<html lang="en">
<head>
<meta charset="utf-8">
<title>Orvessa – Aligner Cleanser Label</title>
<link href="https://fonts.googleapis.com/css2?family=Comfortaa:wght@400;700&family=Oswald:wght@300&display=swap" rel="stylesheet">
<style>
  :root {
    --backdrop: #eef4f0;
    --label-white: #ffffff;
    --label-grey: #e4e6e5;
    --brand-green: #117a2a;
    --wave-green: #4f9a5f;
    --wave-mid: #7fb88a;
    --wave-light: #cfe6d4;
    --mint-teal: #12b89a;
    --gold-light: #f2dfa6;
    --gold-mid: #c9a75a;
    --gold-dark: #7a5c24;
    --sketch-tint: #eaf4ec;
  }
  * { box-sizing: border-box; margin: 0; padding: 0; }
  html, body { width: 900px; height: 1200px; overflow: hidden; }
  body {
    background: var(--backdrop);
    font-family: "Comfortaa", sans-serif;
    color: var(--brand-green);
    position: relative;
  }
  .label-sheet {
    position: absolute;
    left: 40px; top: 330px;
    width: 820px; height: 540px;
    display: flex;
    box-shadow: 0 10px 30px rgba(0,0,0,0.08);
  }
  .panel {
    position: relative;
    width: 410px; height: 540px;
    background: linear-gradient(90deg, var(--label-grey) 0%, var(--label-white) 30%, var(--label-white) 82%, var(--label-grey) 100%);
    overflow: hidden;
  }
  .panel + .panel { border-left: 1px dashed #cfd6d2; }
  .wave { position: absolute; left: 0; bottom: 0; width: 410px; height: 340px; }
  .brand-name {
    position: absolute;
    font-weight: 700;
    color: var(--brand-green);
    line-height: 1;
  }
  .front .brand-name { left: 0; right: 0; top: 78px; text-align: center; font-size: 46px; }
  .back .brand-name { right: 34px; top: 66px; font-size: 22px; }
  .flavour-badge {
    position: absolute; left: 20px; top: 172px;
    width: 52px; height: 52px; border-radius: 50%;
    background: var(--mint-teal);
    color: #fff; font-size: 13px;
    display: flex; align-items: center; justify-content: center;
  }
  .gold-art {
    position: absolute; left: 180px; top: 160px;
    width: 200px; height: 170px;
    border-radius: 80% 20% 40% 60% / 90% 20% 60% 30%;
    background: linear-gradient(150deg, var(--gold-light) 0%, var(--gold-mid) 45%, var(--gold-dark) 100%);
    opacity: 0.8;
  }
  .benefits {
    position: absolute; left: 45px; top: 380px;
    list-style: none;
    font-size: 17px; line-height: 1.3;
  }
  .volume {
    position: absolute; left: 0; right: 0; top: 500px;
    text-align: center;
    font-family: "Oswald", sans-serif; font-weight: 300;
    font-size: 17px; color: #1f5f2c;
  }
  .howto-art {
    position: absolute; left: 22px; top: 40px;
    width: 100px; height: 240px;
    background: linear-gradient(180deg, #f5faf6, var(--sketch-tint));
    border-radius: 6px;
  }
  .steps {
    position: absolute; left: 140px; top: 130px;
    list-style: none; font-size: 12px; line-height: 1.45;
  }
  .usage {
    position: absolute; left: 18px; top: 340px; right: 18px;
    font-size: 10px; line-height: 1.55;
  }
  .usage p + p { margin-top: 14px; padding-left: 14px; }
</style>
</head>
<body>
  <div class="label-sheet">
    <section class="panel front">
      <svg class="wave" viewBox="0 0 410 340" aria-hidden="true">
        <defs>
          <linearGradient id="frontWave" x1="0" x2="1" y1="0" y2="0">
            <stop offset="0" stop-color="var(--wave-green)"/>
            <stop offset="0.7" stop-color="var(--wave-mid)"/>
            <stop offset="1" stop-color="var(--wave-light)"/>
          </linearGradient>
        </defs>
        <path d="M0 40 C70 -10 130 20 190 90 C250 160 330 130 410 80 L410 340 L0 340 Z" fill="url(#frontWave)"/>
      </svg>
      <div class="gold-art" role="img" aria-label="Fan of fine gold lines rising from the wave"></div>
      <h1 class="brand-name">Orvessa</h1>
      <div class="flavour-badge">MINT</div>
      <ul class="benefits">
        <li>Portable Design</li>
        <li>Easy to use</li>
        <li>5 minute Cleaning</li>
        <li>Lasting Freshness</li>
      </ul>
      <p class="volume">1.69 Fl Oz / 50ml</p>
    </section>

    <section class="panel back">
      <svg class="wave" viewBox="0 0 410 340" aria-hidden="true">
        <defs>
          <linearGradient id="backWave" x1="0" x2="1" y1="1" y2="0">
            <stop offset="0" stop-color="var(--wave-green)"/>
            <stop offset="0.6" stop-color="#a9d2b1"/>
            <stop offset="1" stop-color="#eef6f0"/>
          </linearGradient>
        </defs>
        <path d="M0 100 C90 120 150 90 220 40 C290 -5 350 0 410 20 L410 340 L0 340 Z" fill="url(#backWave)"/>
      </svg>
      <div class="howto-art" role="img" aria-label="Five numbered line drawings showing how to clean an aligner"></div>
      <h2 class="brand-name">Orvessa</h2>
      <ol class="steps">
        <li>STEP 1. Remove from mouth</li>
        <li>STEP 2. Spray foam</li>
        <li>STEP 3. Store in the case</li>
        <li>STEP 4. Rinse with water</li>
      </ol>
      <div class="usage">
        <p>Suggested Use:<br>
        Remove clear aligners when eating or drinking.<br>
        Dispense one pump of foam on each aligner.<br>
        Place in the case for five minutes. Then, rinse with<br>
        water and wear back again.</p>
        <p>Use when having:<br>Food / Wine / Coffee</p>
        <p>Made in TaiWan<br>www.Orvessa.com</p>
      </div>
    </section>
  </div>
</body>
</html>
```